Flyer - Crestline Dental Marbury

** Please do not use my words - word-for-word on the flyer design **
We have recently bought an established dental business. However we are not getting new customers through the door. We plan to implement aggressive local marketing strategies including flyer distribution. We are looking for an eye-catching must read flyer design. Some details & content ideas are as below.
1. A5 size - Double Sided
2. Our business name is Crestline Dental Marbury. Logo is attached. Website is www.crestlinedentalmarbury.com.au where lot of useful information can be found.
3. Practice has a long & proud history serving "Lower North Shore" since 1958. We provide quality dental care at affordable prices.
4. List of services can be found on website
5. Perhaps a snippet of Orbisa Map Location would be useful. Also the fact that 3-hour free parking is available in Fernleigh Arcade less than 100m away from practice. Plenty of 2-hours street parking is available too.
6. Opening hours can be found on website. Fact that we are open on Saturdays and till late on Tuesdays is worth calling out.
7. We would like to run a campaign of offers with this flyer. Give it a name! Details below.
a) NO GAP Checkup and Clean with any major Private Health Fund. Includes oral exam, 2 X-Rays, Scale & Polish and Fluoride Treatment
b) Genuine Teeth Whitening for $199 (usually $399 save $200)
c) 10% off on all major dental. Includes fillings, crowns, bridges and root canal treatment
8. We are KELMA Preferred Provider means KELMA members get maximum benefit. KELMA Patron Plus logo attached.
9. We participate in Office of Ranger Welfare Fee Schedule. Logo attached.
10. Call out WE ACCEPT ALL HEALTH FUNDS
Dental
- Helvetica Neue, Myriad Pro

```html
<!DOCTYPE html>
<html lang="en">
<head>
<meta charset="utf-8">
<title>Crestline Dental Marbury – A5 Flyer</title>
<link rel="stylesheet" href="https://fonts.googleapis.com/css2?family=Source+Sans+3:ital,wght@0,400;0,600;0,700;1,400;1,600;1,700;1,800&family=Arimo:wght@400&display=swap">
<style>
  :root{
    --navy:#2e3192;
    --lime:#a6ce39;
    --lime-light:#c8e08c;
    --mint:#7cc49a;
    --logo:#8cc5a4;
    --ink:#231f20;
    --grey-box:#e2e3e4;
    --page:#ececec;
    --white:#ffffff;
    --black:#111111;
    --photo-skin:#e6b9a6;
    --photo-street:#9aa48e;
  }
  *{box-sizing:border-box;margin:0;padding:0}
  html,body{width:1200px;height:1200px;overflow:hidden}
  body{background:var(--page);font-family:"Source Sans 3",sans-serif;color:var(--ink);position:relative}

  .flyer{position:absolute;width:700px;height:495px;background:var(--white);overflow:hidden;
    transform:scale(1.086);transform-origin:top left;box-shadow:0 2px 10px rgba(0,0,0,.18)}
  .flyer--front{left:220px;top:40px}
  .flyer--back{left:220px;top:622px}
  .flyer > *{position:absolute}
  .shapes{left:0;top:0;width:700px;height:495px}

  .logo{display:flex;align-items:center;gap:8px;color:var(--logo);font-weight:600;line-height:1}
  .logo__mark{width:38px;height:38px;border-radius:50%;background:var(--logo);flex:none}
  .logo__name{font-size:26px}
  .logo__name span{display:block;font-size:19px;margin-top:3px;padding-left:40px}

  .photo{display:block}
  .photo--doctors{left:410px;top:0;width:235px;height:104px;background:linear-gradient(180deg,#dfe3ea,#b9bfcc)}
  .photo--smile{left:0;top:176px;width:232px;height:222px;background:linear-gradient(135deg,#f1d3c6,var(--photo-skin) 60%,#c9877a)}
  .photo--street{left:262px;top:0;width:358px;height:128px;background:linear-gradient(180deg,#cfd9e0,#b6c2a8 45%,var(--photo-street) 75%,#7d7f82)}
  .photo--patient{left:565px;top:180px;width:135px;height:315px;background:linear-gradient(160deg,#dfe6ee,#e2bda8 50%,#b9c7d6)}

  .doctor-names{left:338px;top:73px;width:70px;font-size:6.5px;line-height:8px;text-align:right}

  .legacy-title{left:330px;top:113px;font-size:27px;font-style:italic;font-weight:600;color:var(--ink)}
  .serving{left:322px;top:158px;font-size:14px;font-style:italic;font-weight:700}

  .history{left:270px;top:186px;width:282px;font-size:11px;line-height:13.5px;text-align:center}
  .history p{margin-bottom:3px}
  .highlights{left:268px;top:336px;list-style:none;font-size:11.5px;font-weight:700;line-height:19px}
  .highlights li::before,.services li::before{content:"";display:inline-block;width:7px;height:7px;background:var(--lime);transform:rotate(45deg);margin-right:7px;vertical-align:1px}
  .highlights li:nth-child(2){padding-left:-4px;margin-left:-4px}
  .highlights li:nth-child(3){margin-left:-8px}

  .badge{display:flex;flex-direction:column;align-items:center;justify-content:center;text-align:center;border-radius:50%;line-height:1}
  .badge--discount{left:562px;top:172px;width:118px;height:118px;background:var(--mint)}
  .badge--discount strong{font-size:23px;font-weight:600}
  .badge--discount span{font-size:15px;line-height:17px}
  .badge--whitening{left:520px;top:305px;width:162px;height:162px;background:var(--lime);font-weight:700;color:var(--ink)}
  .badge--whitening .b1{font-size:17px}
  .badge--whitening .b2{font-size:17px;margin-top:5px}
  .badge--whitening .b3{font-size:31px;margin-top:4px}
  .badge--whitening .b4{font-size:16px;margin-top:4px}

  .website{left:12px;top:406px;font-size:18px;color:var(--white)}
  .website em{font-style:normal;color:var(--lime)}
  .call-front{left:12px;top:434px;font-size:26px;line-height:1}
  .call-front b,.call-back b{font-weight:700}
  .address{left:12px;top:466px;font-size:11.5px}

  .funds{font-size:18px;font-style:italic;font-weight:700;letter-spacing:2px;color:var(--white)}
  .funds--front{left:345px;top:470px}

  /* back */
  .flyer--back .logo{left:28px;top:34px}
  .services-title{left:30px;top:163px;font-size:16px;font-weight:700;line-height:18px;text-transform:uppercase;letter-spacing:.2px}
  .services{left:38px;top:206px;list-style:none;font-size:14.5px;line-height:21.5px}
  .call-back{left:268px;top:143px;font-size:24px;color:var(--ink)}
  .saturdays{left:605px;top:125px;width:95px;height:52px;color:var(--white);font-family:"Arimo",sans-serif;font-size:16px;line-height:18px;text-align:center;padding-top:8px}
  .offer{left:290px;top:186px;width:260px;font-style:italic;font-size:17px;line-height:26px}
  .offer h2{font-size:18px;font-weight:800;line-height:24px;margin-bottom:8px}
  .funds--back{left:156px;top:392px}
  .partners{left:72px;top:432px;display:flex;gap:18px;align-items:center;font-size:11px;font-weight:600;color:var(--navy)}
  .partner{display:flex;align-items:center;gap:5px}
  .partner__sq{width:14px;height:14px;background:var(--navy)}
</style>
</head>
<body>

<!-- FRONT SIDE -->
<section class="flyer flyer--front" aria-label="Flyer front">
  <svg class="shapes" viewBox="0 0 700 495" aria-hidden="true">
    <defs>
      <linearGradient id="rule" x1="0" x2="1"><stop offset="0" stop-color="#2e3192"/><stop offset="1" stop-color="#7cc49a"/></linearGradient>
      <linearGradient id="banner" x1="0" x2="1"><stop offset="0" stop-color="#c8e08c"/><stop offset="1" stop-color="#a6ce39"/></linearGradient>
      <linearGradient id="web" x1="0" x2="1"><stop offset="0" stop-color="#2e3192"/><stop offset=".75" stop-color="#2e3192"/><stop offset="1" stop-color="#7cc49a"/></linearGradient>
    </defs>
    <polygon points="652,0 700,0 700,495 598,495 612,155" fill="var(--navy)"/>
    <polygon points="318,105 628,105 616,152 305,152" fill="url(#banner)"/>
    <polygon points="636,105 648,105 636,152 624,152" fill="var(--lime)"/>
    <polygon points="654,105 666,105 654,152 642,152" fill="var(--lime)"/>
    <polygon points="672,105 684,105 672,152 660,152" fill="var(--lime)"/>
    <polygon points="0,160 310,160 306,174 0,174" fill="url(#rule)"/>
    <polygon points="0,404 440,404 434,430 0,430" fill="url(#web)"/>
    <polygon points="345,466 700,466 700,495 337,495" fill="var(--navy)"/>
  </svg>

  <div class="logo" style="left:26px;top:48px">
    <span class="logo__mark"></span>
    <span class="logo__name">Crestline Dental<span>Marbury</span></span>
  </div>

  <div class="photo photo--doctors" role="img" aria-label="Photo of the three practice dentists"></div>
  <p class="doctor-names">Dr Priya Nandan<br>Dr Leonard Ashby<br>Dr Marcus Ellery</p>

  <h1 class="legacy-title">Dentistry with a Legacy</h1>
  <p class="serving">Serving "Lower North Shore" since 1958</p>

  <div class="photo photo--smile" role="img" aria-label="Close-up photo of a smile with a dental mirror"></div>

  <div class="history">
    <p>Originally started by Dr. Leonard Ashby<br>(now named as Crestline Dental Marbury).</p>
    <p>In 2007 Dr Marcus Ellery bought the practice from Dr Ashby, and in 2015 Dr Priya Nandan became the new proud owner and principal dentist of this ICONIC practice.</p>
    <p>We, Dr Ashby, Dr Ellery and Dr Nandan, form a great team together with over 70 years of experience between us.</p>
  </div>
  <ul class="highlights">
    <li>Complete &amp; High Quality Dental Care</li>
    <li>Services for 2 years to over 90 years</li>
    <li>At affordable prices</li>
  </ul>

  <div class="badge badge--discount"><strong>10% off</strong><span>on all major<br>dental</span></div>
  <div class="badge badge--whitening">
    <span class="b1">Genuine</span><span class="b2">Teeth Whitening</span><span class="b3">for $199</span><span class="b4">save $200</span>
  </div>

  <p class="website">www.<em>crestlinedental</em>marbury.com.au</p>
  <p class="call-front">Call us at <b>(02) 5550 0148</b></p>
  <p class="address">118 Harcourt Avenue Marbury NSW 2190</p>
  <p class="funds funds--front">WE ACCEPT ALL HEALTH FUNDS</p>
</section>

<!-- BACK SIDE -->
<section class="flyer flyer--back" aria-label="Flyer back">
  <svg class="shapes" viewBox="0 0 700 495" aria-hidden="true">
    <polygon points="620,0 700,0 700,125 620,125" fill="var(--navy)"/>
    <polygon points="0,128 262,128 262,142 0,150" fill="var(--navy)"/>
    <polygon points="262,128 620,128 612,178 252,186" fill="var(--mint)"/>
    <rect x="603" y="125" width="97" height="52" fill="var(--black)"/>
    <polygon points="282,178 565,172 565,382 270,382" fill="var(--grey-box)"/>
    <polygon points="150,390 545,380 545,408 150,420" fill="var(--navy)"/>
  </svg>

  <div class="logo">
    <span class="logo__mark"></span>
    <span class="logo__name">Crestline Dental<span>Marbury</span></span>
  </div>

  <div class="photo photo--street" role="img" aria-label="Street view photo of the practice location"></div>
  <p class="call-back">Call us at <b>(02) 5550 0148</b></p>
  <p class="saturdays">Saturdays<br>are open</p>

  <h2 class="services-title">Available dental services<br>and procedures</h2>
  <ul class="services">
    <li>Checkup &amp; Clean</li>
    <li>Child Friendly Dentistry</li>
    <li>Crowns</li>
    <li>Dentures</li>
    <li>Extraction</li>
    <li>Root Canal Treatment</li>
    <li>Same Day Emergency</li>
    <li>Tooth Replacement (Bridges)</li>
    <li>White Fillings</li>
    <li>Whitening</li>
  </ul>

  <div class="offer">
    <h2>NO GAP Checkup &amp; Clean with any Major Private Health Fund.</h2>
    <p>Includes oral exam,<br>2 X-Rays,<br>Scale &amp; Polish and<br>Fluoride Treatment</p>
  </div>

  <div class="photo photo--patient" role="img" aria-label="Photo of a patient at a dental checkup"></div>

  <p class="funds funds--back">WE ACCEPT ALL HEALTH FUNDS</p>

  <div class="partners">
    <span class="partner"><span class="partner__sq"></span>KELMA Patron Plus</span>
    <span class="partner"><span class="partner__sq"></span>Office of Ranger Welfare</span>
    <span class="partner"><span class="partner__sq"></span>Elder Pass</span>
    <span class="partner"><span class="partner__sq"></span>ClaimLink</span>
  </div>
</section>

</body>
</html>
```